Artificial intelligence, machine learning, and automation company needs a sexy business card design

We need a sleek and sexy business card design for an AI consulting company based in Philadelphia PA. We provide custom machine learning and automation solutions for companies of all shapes and sizes. The primary industries that we serve are pharmaceuticals, engineering, healthcare, and computer software. We would like the designs to be a black business card that uses green as a sleek accent color. The final design should communicate intelligence, cutting edge new-tech, and optimization.

Target Market(s)

C-level and VP level executives of multi-million annual companies. Mostly in Pharma, Healthcare, Real Estate, Retail, and Engineering

Industry/Entity Type

Computer Software

Contact Information for Business Card

Name: Jack Moss
Title: CEO
Cell: 215 604 8293
Email: JackM@quillarcworks.example
Website: www.QuillarcWorks.example

Font styles to use
Sans Serif

Colors

Designer to choose colors to be used in the design.

Requirements
Must have
• 1) Attached Quillarc Logo (either with colors or not/embossed)
• 2) "Artificial Intelligence" "Automation" and "Machine Learning"
• 3) "Quillarc Laboratories" or "Quillarc Works" or "Quillarc"
• 4) Sexy AF.
Nice to have
• Black card / dark card color, "Quillarc Green" accent colors (in attached .ai file), Embossment of logo/name/etc, thick card stock, colored borders (on card sides, not front/back faces)
Should not have
• Should not be bland, or unsexy.

```html
<!DOCTYPE html>
<html lang="en">
<head>
<meta charset="utf-8">
<title>Quillarc Laboratories — Business Card</title>
<link href="https://fonts.googleapis.com/css2?family=Arimo:wght@400;700&display=swap" rel="stylesheet">
<style>
  :root {
    --canvas: #b9b9b9;
    --card-light: #dedede;
    --card-dark: #4a4a4a;
    --ink: #3d3d3d;
    --accent: #4fc3b0;
    --rule: #8a8a8a;
  }
  * { box-sizing: border-box; margin: 0; padding: 0; }
  html, body {
    width: 1200px; height: 896px; overflow: hidden;
    background: var(--canvas);
    font-family: "Arimo", Arial, sans-serif;
  }
  .sheet {
    width: 1200px; height: 896px;
    display: flex; flex-direction: column;
    align-items: center; justify-content: center; gap: 32px;
  }
  .card {
    width: 700px; height: 400px;
    position: relative;
    box-shadow: 0 6px 18px rgba(0,0,0,.25);
  }
  /* Front */
  .card--front {
    background: var(--card-light);
    display: flex; align-items: center;
    padding: 0 48px;
  }
  .brand {
    width: 270px;
    display: flex; align-items: center; gap: 14px;
  }
  .brand__square {
    width: 34px; height: 34px; flex: none;
    background: var(--card-dark);
    border: 5px solid var(--accent);
  }
  .brand__name {
    color: var(--ink);
    font-weight: 400;
    text-transform: uppercase;
    line-height: 1.15;
  }
  .brand__name .line1 { display: block; font-size: 34px; letter-spacing: 6px; }
  .brand__name .line2 { display: block; font-size: 14px; letter-spacing: 5px; }
  .divider {
    width: 1px; height: 150px; background: var(--rule);
    margin: 0 30px 0 20px;
  }
  .contact { color: var(--ink); }
  .contact__name {
    color: var(--accent); font-weight: 700; font-size: 26px;
    text-transform: uppercase; letter-spacing: .5px;
  }
  .contact__title { font-size: 18px; margin-bottom: 14px; }
  .contact__line {
    display: flex; align-items: center; gap: 8px;
    font-size: 15px; line-height: 22px;
  }
  .contact__line svg { width: 14px; height: 14px; flex: none; }
  .services { list-style: none; margin-top: 10px; }
  .services li {
    display: flex; align-items: center; gap: 10px;
    font-size: 14px; line-height: 20px; text-transform: uppercase;
  }
  .services li::before {
    content: ""; width: 10px; height: 10px; background: var(--ink);
  }
  /* Back */
  .card--back {
    background: var(--card-dark);
    display: flex; flex-direction: column;
    align-items: center; justify-content: center; gap: 40px;
  }
  .back-brand {
    display: flex; align-items: center; gap: 18px;
  }
  .back-brand__square {
    width: 46px; height: 46px; border: 6px solid var(--accent);
  }
  .back-brand__name {
    color: var(--accent); font-size: 48px; font-weight: 400;
    letter-spacing: 10px; text-transform: uppercase;
  }
  .back-url {
    color: var(--accent); font-size: 16px; letter-spacing: 6px;
    text-transform: uppercase;
  }
</style>
</head>
<body>
<main class="sheet">
  <section class="card card--front">
    <div class="brand">
      <span class="brand__square"></span>
      <span class="brand__name"><span class="line1">Quillarc</span><span class="line2">Laboratories</span></span>
    </div>
    <div class="divider"></div>
    <div class="contact">
      <h1 class="contact__name">Jack Moss</h1>
      <p class="contact__title">CEO</p>
      <p class="contact__line">
        <svg viewBox="0 0 16 16"><path fill="#4fc3b0" d="M3 2h3l1 4-2 1c1 2 2 3 4 4l1-2 4 1v3c0 1-1 2-2 2C7 15 1 9 1 4c0-1 1-2 2-2z"/></svg>
        215 604 8293
      </p>
      <p class="contact__line">
        <svg viewBox="0 0 16 16"><rect x="1" y="3" width="14" height="10" fill="#4fc3b0"/><path d="M1 3l7 6 7-6" fill="none" stroke="#dedede" stroke-width="1.5"/></svg>
        JackM@quillarcworks.example
      </p>
      <p class="contact__line">
        <svg viewBox="0 0 16 16"><circle cx="8" cy="8" r="7" fill="#4fc3b0"/><path d="M1 8h14M8 1c-3 4-3 10 0 14M8 1c3 4 3 10 0 14" fill="none" stroke="#dedede" stroke-width="1"/></svg>
        www.QuillarcWorks.example
      </p>
      <ul class="services">
        <li>Artificial Intelligence</li>
        <li>Automation</li>
        <li>Machine Learning</li>
      </ul>
    </div>
  </section>

  <section class="card card--back">
    <div class="back-brand">
      <span class="back-brand__square"></span>
      <span class="back-brand__name">Quillarc</span>
    </div>
    <p class="back-url">www.quillarcworks.example</p>
  </section>
</main>
</body>
</html>
```